Postcard Design

We need 6 different postcard designs for our real estate " we buy houses" company based in Washington DC. 3 to use neon colors and 3 to use standard colors. "We buy houses" should always be large on the postcards.
Updates

Hey Guys! I also need every postcard to have the local postal customer box and the retail indicia. take a look at file number 4 titled quick reference guide for the details

Please design using 6.5 x 9 dimension (see Porchlight Parcel Route guideline). You can ignore the provided template from PixelTrove.

-PixelTrove Admin

Target Market(s)

vacant properties, FSBO's, Estate properties, pre foreclosures, divorce

Industry/Entity Type

Real Estate

Requirements
Must have
• quick cash closing
We pay up to $500 referral fee for deals with other sellers

```html
<!DOCTYPE html>
<html lang="en">
<head>
<meta charset="utf-8">
<title>We Buy Houses Postcard – Front and Back</title>
<link rel="stylesheet" href="https://fonts.googleapis.com/css2?family=Anton&family=Arimo:wght@400;700&family=Tinos&display=swap">
<style>
  :root {
    --stage: #000000;
    --card-top: #ffffff;
    --card-bottom: #e4e4e4;
    --ink: #111111;
    --red: #d0021b;
    --yellow: #ffe400;
    --white: #ffffff;
    --tan-light: #eee2bd;
    --tan: #d8c69a;
    --rule: #9a9a9a;
  }
  * { box-sizing: border-box; margin: 0; padding: 0; }
  html, body { width: 1200px; height: 613px; overflow: hidden; background: var(--stage); }
  .stage { position: relative; width: 1200px; height: 613px; background: var(--stage); }

  .postcard {
    position: absolute;
    overflow: hidden;
    background: linear-gradient(180deg, var(--card-top) 0%, var(--card-bottom) 100%);
    font-family: "Arimo", Arial, sans-serif;
  }
  .postcard--front { left: 38px; top: 123px; width: 550px; height: 382px; }
  .postcard--back  { left: 624px; top: 122px; width: 552px; height: 383px; }

  /* Front */
  .headline {
    position: absolute; left: 55px; top: 22px;
    font-family: "Anton", Impact, sans-serif; font-weight: 400;
    font-size: 71px; line-height: 70px;
  }
  .headline__top, .headline__bottom { display: block; transform-origin: left center; white-space: nowrap; }
  .headline__top { color: var(--ink); transform: scaleX(1.23); }
  .headline__bottom { color: var(--red); transform: scaleX(1.4); }

  .badge-quick-cash {
    position: absolute; left: 407px; top: 25px; width: 125px; height: 117px;
    background: linear-gradient(180deg, var(--tan-light) 0%, var(--tan) 100%);
  }
  .badge-quick-cash__text {
    position: absolute; left: 0; top: 50px; width: 100%;
    text-align: center; font-weight: 700; font-size: 14px; line-height: 18.5px; color: var(--ink);
  }

  .referral {
    position: absolute; left: 132px; top: 174px; width: 260px;
    text-align: center; color: var(--ink);
    font-size: 26px; line-height: 26px;
  }
  .referral__amount { display: block; color: var(--red); font-weight: 700; font-size: 34px; line-height: 30px; }

  .photo { position: absolute; }
  .photo--cash-hand { left: 0; top: 190px; width: 162px; height: 130px;
    background: linear-gradient(135deg, #d9c9ac 0%, #a9b59a 50%, #7f9273 100%); }
  .photo--flying-cash { left: 377px; top: 166px; width: 150px; height: 148px;
    background: linear-gradient(180deg, #d7dccf 0%, #c4ccb8 60%, #b8a79a 100%); }

  .contact-bar {
    position: absolute; left: 0; bottom: 0; width: 100%; height: 62px;
    background: var(--red);
  }
  .contact-bar__phone {
    position: absolute; left: 22px; top: 11px;
    display: flex; align-items: center; gap: 6px;
    font-family: "Anton", Impact, sans-serif; font-size: 31px; color: var(--yellow);
  }
  .contact-bar__number { display: inline-block; transform: scaleX(1.14); transform-origin: left center; }
  .contact-bar__divider { position: absolute; left: 265px; top: 14px; width: 1px; height: 34px; background: rgba(255,255,255,0.7); }
  .contact-bar__web {
    position: absolute; left: 292px; top: 21px;
    display: flex; align-items: center; gap: 6px;
    color: var(--white); font-size: 16.5px;
  }

  /* Back */
  .situations__title {
    position: absolute; left: 39px; top: 33px;
    color: var(--red); font-weight: 700; font-size: 16.5px;
  }
  .situations__list {
    position: absolute; left: 39px; top: 66px; list-style: none;
    font-size: 19px; line-height: 21.5px; color: var(--ink);
  }
  .situations__list li { position: relative; padding-left: 16px; }
  .situations__list li::before {
    content: ""; position: absolute; left: 0; top: 8px;
    width: 6px; height: 6px; border-radius: 50%; background: var(--red);
  }
  .photo--house-hand { left: 318px; top: 28px; width: 234px; height: 125px;
    background: linear-gradient(90deg, #f0f0f0 0%, #8c9194 35%, #b89a82 70%, #d6b599 100%); }

  .indicia {
    position: absolute; left: 462px; top: 182px; width: 63px; height: 56px;
    border: 1px solid var(--rule); background: var(--white);
    font-family: "Tinos", "Times New Roman", serif; font-size: 7px; line-height: 8.6px;
    text-align: center; padding-top: 5px; color: var(--ink);
  }

  .back-contact {
    position: absolute; left: 0; top: 268px; width: 299px; height: 115px;
    background: var(--red);
  }
  .back-contact__phone {
    position: absolute; left: 39px; top: 26px; white-space: nowrap;
    font-family: "Anton", Impact, sans-serif; font-size: 34px; line-height: 40px; color: var(--yellow);
    transform: scaleX(1.18); transform-origin: left center;
  }
  .back-contact__web { position: absolute; left: 39px; top: 63px; color: var(--white); font-size: 16.5px; white-space: nowrap; }

  .address-area { position: absolute; left: 299px; top: 268px; width: 253px; height: 115px; background: var(--white); }
  .address-box {
    position: absolute; left: 42px; top: 0; width: 182px; height: 76px;
    border: 1px solid var(--rule);
    font-family: "Tinos", "Times New Roman", serif; color: var(--ink);
  }
  .address-box__route { position: absolute; top: 8px; width: 100%; text-align: center; font-size: 14px; }
  .address-box__recipient { position: absolute; left: 14px; top: 40px; font-size: 14px; line-height: 13px; }
</style>
</head>
<body>
<main class="stage">

  <section class="postcard postcard--front" aria-label="Postcard front">
    <h1 class="headline">
      <span class="headline__top">WE BUY</span>
      <span class="headline__bottom">HOUSES</span>
    </h1>

    <div class="badge-quick-cash" role="img" aria-label="Tan house-shaped sign">
      <p class="badge-quick-cash__text">QUICK<br>CASH<br>CLOSING</p>
    </div>

    <p class="referral">
      We Pay Up To
      <span class="referral__amount">$500</span>
      Referral Fee<br>For Deals With<br>Other Sellers
    </p>

    <div class="photo photo--cash-hand" role="img" aria-label="Hand holding a fan of hundred-dollar bills"></div>
    <div class="photo photo--flying-cash" role="img" aria-label="Small red-roofed house with dollar bills flying around it"></div>

    <footer class="contact-bar">
      <div class="contact-bar__phone">
        <svg width="14" height="24" viewBox="0 0 14 24" aria-hidden="true">
          <path d="M9 1 C3 3 1 8 1 12 C1 16 3 21 9 23 L11 18 L8 16 C6.5 14 6.5 10 8 8 L11 6 Z" fill="var(--white)"/>
        </svg>
        <span class="contact-bar__number">555-013-2468</span>
      </div>
      <span class="contact-bar__divider"></span>
      <div class="contact-bar__web">
        <svg width="14" height="14" viewBox="0 0 14 14" aria-hidden="true" fill="none" stroke="var(--white)" stroke-width="1.2">
          <circle cx="7" cy="7" r="6"/><ellipse cx="7" cy="7" rx="2.6" ry="6"/><line x1="1" y1="7" x2="13" y2="7"/>
        </svg>
        <span>www.harborlineproperties.com</span>
      </div>
    </footer>
  </section>

  <section class="postcard postcard--back" aria-label="Postcard back">
    <h2 class="situations__title">We Specialize In Any Situation</h2>
    <ul class="situations__list">
      <li>Pre forclosures</li>
      <li>Bankrupticies</li>
      <li>Auction properties</li>
      <li>Estate properties</li>
      <li>Landlord owned properties</li>
      <li>For sale by owners</li>
      <li>Handyman specials and</li>
      <li>Vacant properties</li>
    </ul>

    <div class="photo photo--house-hand" role="img" aria-label="Open hand holding a small grey model house"></div>

    <div class="indicia">PRST STD<br>ECRWSS<br>U.S. POSTAGE<br>PAID<br>PPR RETAIL</div>

    <div class="back-contact">
      <p class="back-contact__phone">555-013-2468</p>
      <p class="back-contact__web">www.harborlineproperties.com</p>
    </div>

    <div class="address-area">
      <div class="address-box">
        <p class="address-box__route">****ECRWSS****</p>
        <p class="address-box__recipient">Local<br>Postal Customer</p>
      </div>
    </div>
  </section>

</main>
</body>
</html>
```